Western Canadian Survey Company needs Business Card and Letter Head Design

Hello,

We're looking to have our business cards redesigned along with our letterhead.

We've recently changed out logo and would like to use this. Please use some creativity and propose different options (Traditional and modern).

We will provide as much feedback as possible.

Business card should be double sided with our logo. We would also like room for cell phone number, email address and position. Back of the card can just be our logo or potentially a list of our services we provide.

Industry/Entity Type

Business

Contact Information for Business Card

```html
<!DOCTYPE html>
<html lang="en">
<head>
<meta charset="utf-8">
<title>Northmark Surveys Ltd — Stationery</title>
<link href="https://fonts.googleapis.com/css2?family=Open+Sans:wght@400;600;700&display=swap" rel="stylesheet">
<style>
  :root{
    --slate:#5a7482;
    --ink:#1c1c1c;
    --paper:#fbfbfb;
    --backdrop:#ececec;
    --muted:#6b6b6b;
    --white:#ffffff;
  }
  *{box-sizing:border-box;margin:0;padding:0}
  html,body{width:1200px;height:925px;overflow:hidden}
  body{background:var(--backdrop);font-family:"Open Sans",Arial,sans-serif;position:relative}
  .sheet{position:absolute;background:var(--paper);overflow:hidden}
  .wordmark{display:flex;flex-direction:column;align-items:center;font-weight:700;line-height:1;letter-spacing:.04em;text-transform:uppercase}
  .wordmark .name{display:block}
  .wordmark .tag{display:block;letter-spacing:.18em}

  /* Letterhead */
  .letterhead{left:230px;top:114px;width:341px;height:484px}
  .letterhead .wordmark{position:absolute;top:22px;left:0;right:0;color:var(--slate)}
  .letterhead .name{font-size:12px}
  .letterhead .tag{font-size:5px;margin-top:3px}
  .letterhead .contact{position:absolute;bottom:14px;left:0;right:0;text-align:center;font-size:5.4px;color:var(--muted)}
  .contact b{color:var(--slate);font-weight:600}

  /* Presentation folder */
  .folder{left:630px;top:93px;width:402px;height:509px;background:var(--slate)}
  .folder .spine{position:absolute;left:10px;top:0;bottom:0;width:1px;background:rgba(255,255,255,.12)}
  .folder .wordmark{position:absolute;top:110px;left:0;right:0;color:var(--white)}
  .folder .name{font-size:30px}
  .folder .tag{font-size:8px;margin-top:6px}
  .folder .web-band{position:absolute;left:94px;top:427px;width:308px;height:46px}
  .folder .web-band svg{position:absolute;left:0;top:0}
  .folder .web-band span{position:absolute;right:22px;top:8px;line-height:32px;color:var(--white);font-size:10.5px;letter-spacing:.24em;white-space:nowrap}

  /* Business card front */
  .card-front{left:107px;top:640px;width:154px;height:88px}
  .card-front .wordmark{position:absolute;left:10px;top:33px;width:66px;color:var(--slate)}
  .card-front .name{font-size:8px}
  .card-front .tag{font-size:3.2px;margin-top:2px}
  .card-front .details{position:absolute;left:91px;top:28px;font-size:3.6px;color:var(--muted);line-height:1.55}
  .card-front .person{font-size:5px;color:var(--slate);font-weight:600;line-height:1.2}
  .card-front .role{font-size:3.8px;margin-bottom:3px}
  .card-front .row{display:flex;align-items:center;gap:2px;white-space:nowrap}
  .card-front .row svg{width:4px;height:4px}

  /* Business card back */
  .card-back{left:107px;top:752px;width:155px;height:88px;background:var(--slate)}
  .card-back .wordmark{position:absolute;left:0;right:0;top:30px;color:var(--white)}
  .card-back .name{font-size:11px}
  .card-back .tag{font-size:4px;margin-top:3px}
  .card-back .web{position:absolute;left:0;right:0;bottom:8px;text-align:center;font-size:3.6px;letter-spacing:.4em;color:var(--white)}

  /* Envelope front */
  .envelope-front{left:301px;top:653px;width:381px;height:183px}
  .envelope-front .wordmark{position:absolute;left:16px;top:22px;width:100px;color:var(--slate)}
  .envelope-front .name{font-size:11.5px}
  .envelope-front .tag{font-size:4.5px;margin-top:3px}

  /* Envelope back with flap */
  .envelope-back{left:720px;top:653px;width:381px;height:183px}
  .envelope-back svg{position:absolute;left:0;top:0}
  .envelope-back .wordmark{position:absolute;left:0;right:0;top:24px;color:var(--white)}
  .envelope-back .name{font-size:12px}
  .envelope-back .tag{font-size:4.5px;margin-top:3px}
</style>
</head>
<body>

  <section class="sheet letterhead" aria-label="Letterhead">
    <div class="wordmark"><span class="name">Northmark</span><span class="tag">Surveys Ltd</span></div>
    <p class="contact"><b>Cell :</b> 555 014 2270 &nbsp;|&nbsp; <b>Email :</b> office@northmarksurveys.ca &nbsp;|&nbsp; <b>Web :</b> www.northmarksurveys.ca</p>
  </section>

  <section class="sheet folder" aria-label="Presentation folder">
    <div class="spine"></div>
    <div class="wordmark"><span class="name">Northmark</span><span class="tag">Surveys Ltd</span></div>
    <div class="web-band">
      <svg width="308" height="46" viewBox="0 0 308 46" aria-hidden="true">
        <polygon points="0,23 22,0 22,8 308,8 308,40 22,40 22,46" fill="var(--ink)"/>
      </svg>
      <span>www.northmarksurveys.ca</span>
    </div>
  </section>

  <section class="sheet card-front" aria-label="Business card front">
    <div class="wordmark"><span class="name">Northmark</span><span class="tag">Surveys Ltd</span></div>
    <div class="details">
      <div class="person">DANA FERRIS</div>
      <div class="role">CEO/Founder</div>
      <div class="row"><svg viewBox="0 0 4 4"><rect x="1" y="0" width="2" height="4" rx=".4" fill="none" stroke="currentColor" stroke-width=".5"/></svg>555 014 2270</div>
      <div class="row"><svg viewBox="0 0 4 4"><rect x=".3" y=".8" width="3.4" height="2.4" fill="none" stroke="currentColor" stroke-width=".5"/></svg>office@northmarksurveys.ca</div>
      <div class="row"><svg viewBox="0 0 4 4"><circle cx="2" cy="2" r="1.6" fill="none" stroke="currentColor" stroke-width=".5"/></svg>www.northmarksurveys.ca</div>
    </div>
  </section>

  <section class="sheet card-back" aria-label="Business card back">
    <div class="wordmark"><span class="name">Northmark</span><span class="tag">Surveys Ltd</span></div>
    <p class="web">www.northmarksurveys.ca</p>
  </section>

  <section class="sheet envelope-front" aria-label="Envelope front">
    <div class="wordmark"><span class="name">Northmark</span><span class="tag">Surveys Ltd</span></div>
  </section>

  <section class="sheet envelope-back" aria-label="Envelope back">
    <svg width="381" height="183" viewBox="0 0 381 183" aria-hidden="true">
      <path d="M0 0 H381 L370 58 Q367 63 360 63 H21 Q14 63 11 58 Z" fill="var(--slate)"/>
    </svg>
    <div class="wordmark"><span class="name">Northmark</span><span class="tag">Surveys Ltd</span></div>
  </section>

</body>
</html>
```